2 Elite Law Firms on 1 double-sided monument Sign

The original story: 2 separate law firms already have their own perfect individual sign monuments, one for each firm. However, we must now combine them into 1 monument.

Target Market(s)

high-end clientele

Industry/Entity Type

Legal

Requirements
Must have
• Sleek, equal representation of both firms.

```html
<!DOCTYPE html>
<html lang="en">
<head>
<meta charset="utf-8">
<title>Shared Monument Sign – Marlow Law Group &amp; Whitfield &amp; Associates</title>
<link href="https://fonts.googleapis.com/css2?family=Cinzel:wght@400;600&family=Roboto+Condensed:wght@400&display=swap" rel="stylesheet">
<style>
  :root {
    --paper: #ffffff;
    --navy: #022a5e;
    --navy-deep: #031a3c;
    --black: #000000;
    --ink: #ffffff;
    --plinth: #9b9b9b;
    --ground: #555555;
  }
  * { margin: 0; padding: 0; box-sizing: border-box; }
  html, body { width: 1200px; height: 751px; overflow: hidden; background: var(--paper); }
  .elevation { position: relative; width: 1200px; height: 751px; }

  .ground-line { position: absolute; left: 109px; top: 593px; width: 980px; height: 1px; background: var(--ground); }
  .plinth { position: absolute; top: 494px; height: 99px; background: var(--plinth); }
  .plinth--wide { left: 193px; width: 476px; }
  .plinth--narrow { left: 860px; width: 119px; }

  .sign-face {
    position: absolute; top: 157px; height: 337px; color: var(--ink);
    background: linear-gradient(52deg, var(--navy-deep) 0%, var(--navy) 22%, #021a3d 48%, var(--black) 88%);
  }
  .sign-face--wide { left: 134px; width: 595px; }
  .sign-face--narrow { left: 830px; width: 179px;
    background: linear-gradient(62deg, var(--navy-deep) 0%, var(--navy) 28%, #021a3d 55%, var(--black) 92%); }

  .centered { position: absolute; transform: translateX(-50%); text-align: center; white-space: nowrap; }

  .suite-number { font-family: "Cinzel", serif; font-weight: 600; font-size: 22px; line-height: 1; letter-spacing: 1px; }

  .divider-vertical { position: absolute; left: 296px; top: 36px; width: 3px; height: 257px; border-radius: 2px; background: var(--ink); }
  .divider-horizontal { position: absolute; left: 27px; top: 167px; width: 126px; height: 3px; border-radius: 2px; background: var(--ink); }

  .firm-name { font-family: "Cinzel", serif; font-weight: 400; line-height: 1; }
  .marlow-name { font-size: 42px; letter-spacing: 2px; }
  .marlow-sub { font-size: 14px; letter-spacing: 6px; }
  .whitfield-name { font-size: 38px; letter-spacing: 2px; }
  .whitfield-sub { font-size: 32px; letter-spacing: 2px; }

  .practice-list, .firm-tag { font-family: "Roboto Condensed", sans-serif; font-size: 10px; line-height: 16px; letter-spacing: 0.1px; }
  .firm-tag { line-height: 12px; }
  .practice-list span + span { margin-left: 8px; }
  .web-address { font-family: "Roboto Condensed", sans-serif; font-size: 12.5px; line-height: 1; }

  .mark-square { display: inline-block; width: 10px; height: 10px; border: 2px solid var(--ink); margin-right: 8px; vertical-align: 6px; }
</style>
</head>
<body>
<main class="elevation">
  <div class="plinth plinth--wide"></div>
  <div class="plinth plinth--narrow"></div>
  <div class="ground-line"></div>

  <section class="sign-face sign-face--wide">
    <div class="centered suite-number" style="left:149px; top:26px;">418</div>
    <div class="divider-vertical"></div>
    <div class="centered suite-number" style="left:446px; top:26px;">420</div>

    <div class="centered firm-name marlow-name" style="left:157px; top:116px;"><span class="mark-square"></span>MARLOW</div>
    <div class="centered firm-name marlow-sub" style="left:165px; top:170px;">LAW GROUP</div>
    <div class="centered practice-list" style="left:157px; top:215px;">
      <div><span>DWI/DUI</span><span>TRAFFIC</span></div>
      <div><span>CRIMINAL</span><span>LITIGATION</span></div>
      <div><span>IMMIGRATION</span></div>
    </div>
    <div class="centered web-address" style="left:157px; top:298px;">MarlowLawGroup.com</div>

    <div class="centered firm-name whitfield-name" style="left:446px; top:113px;">WHITFIELD</div>
    <div class="centered firm-name whitfield-sub" style="left:446px; top:150px;">&amp; ASSOCIATES</div>
    <div class="centered firm-tag" style="left:446px; top:226px;">PERSONAL INJURY<br>LAW FIRM</div>
    <div class="centered web-address" style="left:444px; top:298px;">WhitfieldAndAssociatesLaw.com</div>
  </section>

  <section class="sign-face sign-face--narrow">
    <div class="centered suite-number" style="left:90px; top:18px;">418</div>
    <div class="centered firm-name" style="left:90px; top:92px; font-size:26px; letter-spacing:1px;">MARLOW</div>
    <div class="centered firm-name" style="left:92px; top:123px; font-size:9px; letter-spacing:4px;">LAW GROUP</div>
    <div class="divider-horizontal"></div>
    <div class="centered firm-name" style="left:90px; top:210px; font-size:44px;">W&amp;A</div>
    <div class="centered suite-number" style="left:90px; top:294px;">420</div>
  </section>
</main>
</body>
</html>
```